New Branding Concept Healthcare Course Brochure

OBJECTIVE:
We need a new course brochure design to meet match our new branding colour scheme & concept as we are currently in the process of upgrading our website design. This A4 double sided brochure will briefly showcase a course on offer, in a clear, concise, professional and engaging way. This brochure will be in line with our new branding colour scheme and concept.
Our concept in monochrome with spashes & pops of colour (matching our logo colours) - see examples attached of imagery being used for social media currently as this somewhat reflects the concept we are working towards after, in terms of colour and look.

We are happy for you to be creative with formats. However, it must be able to include the same information as attached in "disability course brochure information". Have also attached some 'format examples' that we like - this is purely for ideas of paragraphing and formatting of information that other training providers are using, not for colour and graphic examples.

The final design will be used for promotional and adverting purposes to communicate information about a course to a prospective student in both print and soft copy form.

ORGANISATION OVERVIEW:
Verity Lane Institute (RTO.47381)
03 9417 2658
www.veritylaneinstitute.edu.au
admin@vli.edu.au
Head Office (Admin only): Level 2, 48 Marlowe Street, Blackburn VIC 3130
3 modern & fully equipped training campuses across Melbourne: Blackburn (Kestrel Road), Preston & Narre Warren.
We are a private registered training organisation based in Melbourne, Victoria, Australia specialising in only healthcare courses such as certificate III in pathology collection, Certificate IV in Disability, Certificate III in individual Support, Certificate IV in Aged Care & Certificate III in Health Services Assistance. We also offer professional development training workshops to corporate clients and the public such as first aid, cpr, medications, food saftey, manual handling and much more.

Target Market(s)

Prospective Healthcare Education Students

Font styles to use
Serif

Colors
f37122
fbed22
ffffff

Requirements
Must have
• MUST INCLUDE:
- ZPX Logo (attached)
- Our Logo (attached)
- Our slogan (Making you the future of healthcare)
- QR Code
- pops of colour must match our logo colours (see guide attached)
- contact details: website, social media buttons (instagram, facebook & twitter), phone number, email & our head office address.
- Must include relevant imagery (in this case disability or disability carer related, steer away from wheelchair images as it's used too much)
- must include information items (as per attached "disability brochure course information"

```html
<!DOCTYPE html>
<html lang="en">
<head>
<meta charset="utf-8">
<title>CHC43115 Certificate IV in Disability</title>
<link href="https://fonts.googleapis.com/css2?family=Source+Sans+3:ital,wght@0,400;0,600;0,700;1,700&display=swap" rel="stylesheet">
<style>
  :root {
    --accent: #e8542b;
    --accent-orange: #f37122;
    --accent-yellow: #fbed22;
    --ink: #3a3a3a;
    --muted: #6b6b6b;
    --paper: #ffffff;
    --band: #f2f2f2;
    --photo-a: #8c8f93;
    --photo-b: #ddd6cf;
    --photo-c: #6f6a66;
  }
  * { margin: 0; padding: 0; box-sizing: border-box; }
  html, body { width: 849px; height: 1200px; overflow: hidden; background: var(--paper); }
  body { font-family: "Source Sans 3", Arial, sans-serif; color: var(--ink); }
  .page { position: relative; width: 849px; height: 1200px; }

  .course-code { position: absolute; left: 34px; top: 22px; font-size: 31px; line-height: 36px; font-weight: 400; color: var(--muted); }
  .course-title { position: absolute; left: 34px; top: 58px; font-size: 31px; line-height: 33px; font-weight: 700; color: var(--accent); text-transform: uppercase; }

  .logo-partner { position: absolute; left: 596px; top: 30px; display: flex; align-items: center; gap: 6px; font-size: 16px; font-weight: 700; color: var(--accent); }
  .logo-partner .mark { width: 14px; height: 14px; background: var(--accent); }
  .logo-brand { position: absolute; left: 700px; top: 30px; width: 120px; display: flex; align-items: flex-start; gap: 6px; font-size: 15px; line-height: 17px; font-weight: 700; color: var(--accent-orange); }
  .logo-brand .mark { flex: none; width: 13px; height: 13px; border-radius: 50%; background: var(--accent-yellow); margin-top: 2px; }

  .hero { position: absolute; left: 0; top: 141px; width: 849px; height: 416px; background: linear-gradient(115deg, var(--photo-c) 0%, var(--photo-a) 30%, var(--photo-b) 60%, #b9b0a8 100%); }
  .hero-caption { position: absolute; left: 34px; top: 508px; width: 320px; font-size: 12px; line-height: 15px; color: var(--paper); }

  .col-main { position: absolute; left: 34px; top: 572px; width: 486px; }
  .col-side { position: absolute; left: 553px; top: 572px; width: 270px; }
  h2 { font-size: 17px; line-height: 22px; font-weight: 700; color: var(--accent); margin-bottom: 5px; }
  p, li { font-size: 16px; line-height: 20px; }
  p + p { margin-top: 11px; }
  .block { margin-top: 16px; }
  .block-wide { margin-top: 20px; }
  ul { list-style: none; }
  li::before { content: "\2022"; margin-right: 6px; }
  .note { margin-top: 11px; }
  .link { font-weight: 700; }
  .mode-label { font-weight: 700; font-style: italic; color: var(--accent); }

  .footer { position: absolute; left: 0; top: 1076px; width: 849px; height: 124px; background: var(--band); border-top: 4px solid var(--accent-orange); }
  .slogan { position: absolute; left: 34px; top: 18px; font-size: 19px; font-weight: 700; color: var(--accent); }
  .contacts { position: absolute; left: 34px; top: 50px; width: 560px; font-size: 13.5px; line-height: 18px; color: var(--ink); }
  .contacts strong { color: var(--accent); font-weight: 700; }
  .socials { position: absolute; left: 620px; top: 44px; display: flex; gap: 8px; }
  .socials span { width: 26px; height: 26px; border-radius: 50%; background: var(--accent-orange); }
  .qr { position: absolute; left: 725px; top: 14px; width: 90px; height: 90px; background: var(--paper); border: 3px solid var(--ink); }
</style>
</head>
<body>
<div class="page">
  <div class="course-code">CHC43115</div>
  <h1 class="course-title">Certificate IV<br>in Disability</h1>

  <div class="logo-partner"><span class="mark"></span>ZPX</div>
  <div class="logo-brand"><span class="mark"></span>Verity Lane Institute</div>

  <div class="hero" role="img" aria-label="Photo of a disability support worker kindly assisting an older woman indoors"></div>
  <p class="hero-caption">Start your rewarding career in disability with Verity Lane Institute and become a job-ready disability support worker (DSW)</p>

  <section class="col-main">
    <h2>Course Overview</h2>
    <p>This qualification reflects the role of workers in a range of community settings and clients’ homes, who provide training and support in a manner that empowers people with disabilities to achieve greater levels of independence, community participation and wellbeing, workers promote a person-centred approach and more.</p>
    <p>Verity Lane Institute is committed to providing an inclusive learning environment. Principles of access and equity for all students are applied in all programs. People with disabilities are encouraged to apply.</p>

    <div class="block">
      <h2>Duration</h2>
      <ul>
        <li>22 weeks* of 1 day per week (9am–4.30pm) or</li>
        <li>30 weeks* of 1 evening per week (5pm–9pm) + 3 Saturdays (9am–4:30pm)</li>
      </ul>
      <p class="note">Delivery location &amp; duration varies between intakes. Please refer to our website at <span class="link">www.veritylaneinstitute.edu.au</span> for upcoming course availability</p>
    </div>

    <div class="block-wide">
      <p><span class="mode-label">Delivery Mode:</span> Classroom &amp; blended/virtual learning</p>
      <p>Practical experience and assessment is undertaken throughout the course in the Verity Lane Institute simulated environment with trainers who are experts in their field and maintain currency in the industry.</p>
    </div>
  </section>

  <aside class="col-side">
    <h2>Job Prospects</h2>
    <p>Possible outcomes may include:</p>
    <ul>
      <li>Community Worker</li>
      <li>Disabilities Services Officer</li>
      <li>Disability Support Worker</li>
    </ul>
    <div class="block-wide">
      <h2>Delivery Locations</h2>
      <p>Blackburn, Narre Warren &amp; Preston</p>
    </div>
  </aside>

  <footer class="footer">
    <div class="slogan">Making you the future of healthcare</div>
    <div class="contacts">
      <strong>P</strong> 03 9417 2658 &nbsp;&nbsp; <strong>E</strong> admin@vli.edu.au &nbsp;&nbsp; <strong>W</strong> www.veritylaneinstitute.edu.au<br>
      Head Office (Admin only): Level 2, 48 Marlowe Street, Blackburn VIC 3130<br>
      Verity Lane Institute (RTO.47381)
    </div>
    <div class="socials" aria-label="Social media links">
      <span aria-label="Social link one"></span>
      <span aria-label="Social link two"></span>
      <span aria-label="Social link three"></span>
    </div>
    <div class="qr" role="img" aria-label="QR code linking to the course page"></div>
  </footer>
</div>
</body>
</html>
```